Upgrades and adjustments to my existing website

I currently have a website in the trial period with HostBramble but their template isn't meeting my site needs. My website is https://www.QuorvaPosts.example. I need the calendar to be changed. Each customer that orders a real estate sign installation from us needs to be able to request a day (not time specific) and be able to enter the address of the home where they need the sign installed. In addition, I would like a testimonials section on the website. I need someone to build the website and point it to my domain name as I do not know how to do any of that. My customers are trying to order now so every day they can't place the order I am losing money so quick turn time is important

Target Market(s)

Real Estate Agents ordering sign post installations

Industry/Entity Type

Real Estate

Coding

Coded - Design and coding required

Number of Pages Required

1 page

Font styles to use
Sans Serif

Colors
0355a3
3377b5
85abd2
0493ce
33a6d7
85cae6

Requirements
Must have
• The ability to book installation requests online with address for installation. Please see live current website I have
Nice to have
• Links to social media, ability to pay invoice on website,
Testimonial section.
Ability to track progress of installation request for customers
Ability to share the appointment calendar with my installers

```html
<!DOCTYPE html>
<html lang="en">
<head>
<meta charset="utf-8">
<title>Quorva Posts – Real Estate Sign Installation</title>
<link href="https://fonts.googleapis.com/css2?family=Lato:wght@400;700;900&display=swap" rel="stylesheet">
<style>
:root{
  --blue-deep:#0355a3;
  --blue-mid:#3377b5;
  --blue-soft:#85abd2;
  --cyan:#0493ce;
  --cyan-mid:#33a6d7;
  --cyan-soft:#85cae6;
  --btn:#1c6fe0;
  --navy:#0b1d36;
  --ink:#1f2633;
  --muted:#8a93a3;
  --tint:#eef2f7;
  --white:#ffffff;
  --star:#f2a516;
}
*{box-sizing:border-box;margin:0;padding:0}
html,body{width:1200px;height:2660px;overflow:hidden}
body{font-family:'Lato',Arial,sans-serif;color:var(--ink);background:var(--white);position:relative}
.btn{display:inline-block;background:var(--btn);color:var(--white);font-weight:700;font-size:15px;letter-spacing:.5px;padding:14px 22px;border-radius:3px;text-transform:uppercase}

/* hero */
.hero{position:absolute;left:0;top:0;width:1200px;height:660px;overflow:hidden}
.hero-photo{position:absolute;inset:0;background:linear-gradient(100deg,#14213a 0%,#2b3a4d 40%,#6a5546 70%,#8a6a52 100%)}
.hero-shade{position:absolute;inset:0;background:linear-gradient(90deg,rgba(8,18,36,.75) 0%,rgba(8,18,36,.35) 55%,rgba(8,18,36,.1) 100%)}
.nav{position:absolute;left:0;top:0;width:100%;height:80px;display:flex;align-items:center;padding:0 130px}
.brand{display:flex;align-items:center;gap:10px;color:var(--white);font-weight:900;font-size:22px}
.brand-mark{width:22px;height:22px;background:var(--cyan)}
.nav-links{margin-left:auto;display:flex;align-items:center;gap:34px;font-size:15px;color:var(--white)}
.nav-links .active{border-bottom:2px solid var(--white);padding-bottom:4px}
.nav-links .btn{font-size:14px;padding:12px 18px}
.hero-copy{position:absolute;left:130px;top:245px;color:var(--white)}
.hero-copy h1{font-size:104px;font-weight:900;letter-spacing:1px;line-height:1}
.hero-copy p{font-size:34px;font-weight:700;margin:22px 0 40px}
.dots{position:absolute;left:50%;top:600px;transform:translateX(-50%);display:flex;gap:8px}
.dots span{width:9px;height:9px;border-radius:50%;background:rgba(255,255,255,.5)}
.dots span:first-child{background:var(--white)}

/* about */
.about{position:absolute;left:0;top:660px;width:1200px;height:540px}
.about-photo{position:absolute;left:0;top:0;width:590px;height:540px;background:linear-gradient(160deg,#8fa7c4 0%,#6d6a6e 55%,#5b4a3c 100%)}
.about-copy{position:absolute;left:655px;top:140px;width:420px}
.about-copy h2{font-size:46px;font-weight:900;text-transform:uppercase}
.about-copy h2 span{color:var(--btn)}
.about-copy p{font-size:14px;line-height:1.75;color:var(--muted);margin:24px 0 30px}

/* appointments */
.appointments{position:absolute;left:0;top:1200px;width:1200px;height:640px;background:var(--tint)}
.section-title{text-align:center;font-size:46px;font-weight:900;text-transform:uppercase;color:var(--ink)}
.section-title span{color:var(--btn)}
.appointments .section-title{margin-top:115px}
.appointments .lead{text-align:center;font-size:18px;color:#555e6c;margin-top:14px}
.booking{position:absolute;left:185px;top:350px;width:830px;height:420px;background:var(--white);box-shadow:0 4px 18px rgba(20,40,80,.08);display:flex;padding:20px}
.calendar{width:430px;border-right:1px solid #e3e7ee;padding-right:20px}
.cal-head{margin:0 auto;width:230px;height:32px;background:var(--navy);color:var(--white);display:flex;align-items:center;justify-content:space-between;padding:0 12px;font-size:14px;font-weight:700;letter-spacing:.5px}
.cal-grid{display:grid;grid-template-columns:repeat(7,1fr);row-gap:14px;margin-top:24px;text-align:center;font-size:13px;color:#444}
.cal-grid .dow{font-weight:700;font-size:12px;color:var(--ink)}
.cal-grid .day{width:28px;height:28px;line-height:28px;margin:0 auto;border-radius:50%}
.cal-grid .seen{background:#d7dbe2}
.cal-grid .pick{background:var(--btn);color:var(--white)}
.cal-grid .today{background:var(--navy);color:var(--white)}
.cal-form{display:flex;margin-top:26px}
.cal-form .field{flex:1;height:42px;border:1px solid var(--btn);padding:0 12px;line-height:40px;font-size:13px;color:var(--muted)}
.cal-form .btn{padding:0 18px;line-height:42px;font-size:13px;border-radius:0}
.services{flex:1;padding-left:22px;display:flex;flex-direction:column;gap:20px}
.service{display:flex;gap:18px;height:180px}
.service-photo{width:150px;height:180px;background:linear-gradient(180deg,#d9dde2,#8a8f96)}
.service:last-child .service-photo{background:linear-gradient(180deg,#3b3f46,#9ba1a9)}
.service-info{padding-top:40px}
.service-info h3{font-size:18px;font-weight:700;line-height:1.3}
.service-info .meta{display:flex;align-items:center;gap:6px;font-size:11px;color:var(--muted);margin:10px 0 14px}
.service-info .btn{font-size:12px;padding:10px 14px}

/* testimonials */
.testimonials{position:absolute;left:0;top:1840px;width:1200px;height:530px}
.testimonials .section-title{margin-top:150px}
.quotes{position:absolute;left:130px;top:280px;width:940px;display:flex;gap:40px}
.quote{flex:1;display:flex;gap:16px}
.avatar{width:60px;height:60px;border-radius:50%;background:linear-gradient(160deg,#c9b6a6,#7b6a5f);flex:none}
.quote p{font-size:11.5px;line-height:1.55;color:var(--muted)}
.quote .name{font-size:11px;font-weight:700;color:var(--ink);margin-top:10px;text-transform:uppercase}
.quote .role{font-size:10.5px;color:var(--muted)}
.stars{color:var(--star);font-size:15px;letter-spacing:2px;margin-top:8px}
.arrow{position:absolute;top:300px;width:32px;height:32px;border-radius:50%;background:#e6e9ee;display:flex;align-items:center;justify-content:center}
.arrow.prev{left:62px}.arrow.next{right:62px}

/* footer */
.footer{position:absolute;left:0;top:2370px;width:1200px;height:290px;background:var(--navy);color:var(--white)}
.contacts{position:absolute;left:235px;top:40px;width:730px;display:flex;align-items:center;justify-content:space-between;font-size:15px}
.contact{display:flex;align-items:center;gap:14px}
.contact .icon{width:44px;height:44px;border-radius:50%;background:var(--btn);display:flex;align-items:center;justify-content:center}
.contact small{display:block;font-size:14px}
.foot-nav{position:absolute;left:0;top:135px;width:100%;text-align:center;font-size:20px;font-weight:700;letter-spacing:.5px}
.foot-nav span{margin:0 10px}
.foot-bar{position:absolute;left:130px;top:220px;width:940px;border-top:1px solid rgba(255,255,255,.15);padding-top:22px;display:flex;justify-content:space-between;align-items:center;font-size:11px;color:#c4ccd8}
.social{width:22px;height:22px;border-radius:50%;border:1px solid #c4ccd8}
</style>
</head>
<body>

<header class="hero">
  <div class="hero-photo" role="img" aria-label="Brick house front with a red and white For Sale sign on a post in the yard"></div>
  <div class="hero-shade"></div>
  <nav class="nav">
    <div class="brand"><span class="brand-mark"></span>Quorva Posts</div>
    <div class="nav-links">
      <span class="active">Home</span><span>About Us</span><span>Events</span><span>Contact Us</span>
      <span class="btn">Online Appointment</span>
    </div>
  </nav>
  <div class="hero-copy">
    <h1>QUORVA POSTS</h1>
    <p>Don't sell your home in the dark</p>
    <span class="btn">Online Appointment</span>
  </div>
  <div class="dots"><span></span><span></span><span></span><span></span></div>
</header>

<section class="about">
  <div class="about-photo" role="img" aria-label="Installer standing beside a newly placed For Sale sign post on a front lawn"></div>
  <div class="about-copy">
    <h2>About <span>Quorva Posts</span></h2>
    <p>We install sign posts for real estate agents so every listing stands out day and night. Our crews set each post level and secure, keep it in good shape, and remove it once the home is sold. Local, reliable, and focused on great service every time.</p>
    <span class="btn">Read More</span>
  </div>
</section>

<section class="appointments">
  <h2 class="section-title">Online <span>Appointments</span></h2>
  <p class="lead">Select any time and we will install within 48 hours</p>
  <div class="booking">
    <div class="calendar">
      <div class="cal-head"><span>&#8249;</span>MARCH 2021<span>&#8250;</span></div>
      <div class="cal-grid">
        <span class="dow">MON</span><span class="dow">TUE</span><span class="dow">WED</span><span class="dow">THU</span><span class="dow">FRI</span><span class="dow">SAT</span><span class="dow">SUN</span>
        <span class="day">1</span><span class="day">2</span><span class="day">3</span><span class="day">4</span><span class="day">5</span><span class="day">6</span><span class="day">7</span>
        <span class="day">8</span><span class="day seen">9</span><span class="day">10</span><span class="day">11</span><span class="day">12</span><span class="day">13</span><span class="day pick">14</span>
        <span class="day">15</span><span class="day">16</span><span class="day">17</span><span class="day">18</span><span class="day">19</span><span class="day">20</span><span class="day today">21</span>
        <span class="day">22</span><span class="day">23</span><span class="day">24</span><span class="day">25</span><span class="day">26</span><span class="day">27</span><span class="day">28</span>
        <span class="day">29</span><span class="day">30</span><span class="day">31</span>
      </div>
      <div class="cal-form">
        <div class="field">Enter Address</div>
        <span class="btn">Request a Day</span>
      </div>
    </div>
    <div class="services">
      <div class="service">
        <div class="service-photo" role="img" aria-label="Real estate sign post installed beside a house"></div>
        <div class="service-info">
          <h3>Real Estate Sign<br>Installation</h3>
          <div class="meta"><svg width="11" height="11" viewBox="0 0 12 12"><circle cx="6" cy="6" r="5" fill="none" stroke="#8a93a3" stroke-width="1.4"/><path d="M6 3v3l2 1.5" stroke="#8a93a3" stroke-width="1.4" fill="none"/></svg>Install within 48 hrs</div>
          <span class="btn">Schedule Here</span>
        </div>
      </div>
      <div class="service">
        <div class="service-photo" role="img" aria-label="Sign post being taken down from a yard"></div>
        <div class="service-info">
          <h3>Sign Removal</h3>
          <div class="meta"><svg width="11" height="11" viewBox="0 0 12 12"><circle cx="6" cy="6" r="5" fill="none" stroke="#8a93a3" stroke-width="1.4"/><path d="M6 3v3l2 1.5" stroke="#8a93a3" stroke-width="1.4" fill="none"/></svg>Pickup on request</div>
          <span class="btn">Schedule Here</span>
        </div>
      </div>
    </div>
  </div>
</section>

<section class="testimonials">
  <h2 class="section-title">Customer <span>Testimonials</span></h2>
  <div class="arrow prev"><svg width="10" height="10" viewBox="0 0 10 10"><path d="M6.5 1.5L3 5l3.5 3.5" stroke="#555" stroke-width="1.6" fill="none"/></svg></div>
  <div class="arrow next"><svg width="10" height="10" viewBox="0 0 10 10"><path d="M3.5 1.5L7 5 3.5 8.5" stroke="#555" stroke-width="1.6" fill="none"/></svg></div>
  <div class="quotes">
    <div class="quote">
      <div class="avatar" role="img" aria-label="Customer portrait"></div>
      <div>
        <p>Fast install and clean work. The post went up the day I asked and my sellers loved how the sign looked.</p>
        <div class="name">Amanda Cole</div><div class="role">Listing Agent</div>
        <div class="stars">★★★★☆</div>
      </div>
    </div>
    <div class="quote">
      <div class="avatar" role="img" aria-label="Customer portrait"></div>
      <div>
        <p>Booking a day online is so easy. I enter the address and the sign is in place within two days.</p>
        <div class="name">Marcus Reed</div><div class="role">Home Broker</div>
        <div class="stars">★★★★☆</div>
      </div>
    </div>
    <div class="quote">
      <div class="avatar" role="img" aria-label="Customer portrait"></div>
      <div>
        <p>Friendly crew and quick removal after closing. I use them for every listing and would recommend them to any agent.</p>
        <div class="name">Dana Price</div><div class="role">Realty Partner</div>
        <div class="stars">★★★★☆</div>
      </div>
    </div>
  </div>
</section>

<footer class="footer">
  <div class="contacts">
    <div class="contact">
      <span class="icon"><svg width="20" height="20" viewBox="0 0 20 20"><circle cx="10" cy="10" r="7.5" fill="none" stroke="#fff" stroke-width="1.8"/><path d="M10 5.5V10l3 2" stroke="#fff" stroke-width="1.8" fill="none"/></svg></span>
      <div>Open today<small>08:00 am – 10:00 pm</small></div>
    </div>
    <div class="contact">
      <svg width="18" height="18" viewBox="0 0 20 20"><path d="M5 2l3 4-2 2c1 2.5 3.5 5 6 6l2-2 4 3-2 3C9 17 3 11 2 4z" fill="#fff"/></svg>
      555-014-2290
    </div>
    <div class="contact">
      <span class="icon"><svg width="20" height="16" viewBox="0 0 20 16"><rect x="1.5" y="1.5" width="17" height="13" rx="1" fill="none" stroke="#fff" stroke-width="1.6"/><path d="M2 2l8 7 8-7" stroke="#fff" stroke-width="1.6" fill="none"/></svg></span>
      Orders@QuorvaPosts.example
    </div>
  </div>
  <div class="foot-nav"><span>HOME</span>/<span>ABOUT US</span>/<span>EVENTS</span>/<span>CONTACT US</span></div>
  <div class="foot-bar">
    <span>Copyright © 2021, Quorva Posts. All rights reserved. | Privacy Policy | Terms of Use</span>
    <span class="social"></span>
  </div>
</footer>

</body>
</html>
```